Korvane - Business Card Design

Design a modern masculine business card for our business

Target Market(s)

Private Market

Industry/Entity Type

Construction

Contact Information for Business Card

Company Name - Name of Person - Address - email address - contact number

Font styles to use
Serif
Sans Serif

Colors
0094D4
00A9DD
6FCCEA
C7EBF8
E9F6FB
00AB8E
00BBA5
67D7C9
C6EFE9
E9F9F6
F0912C
F2A743
F7CA91
FBE8D2
FDF5EE

Requirements
Must have
• Use company logo provided
Nice to have
• Company Logo

```html
<!DOCTYPE html>
<html lang="en">
<head>
<meta charset="utf-8">
<title>Korvane – Business Card</title>
<link href="https://fonts.googleapis.com/css2?family=Montserrat:wght@500;700;800&family=Quicksand:wght@400;500&display=swap" rel="stylesheet">
<style>
  :root {
    --backdrop: #e9e6e2;
    --ink: #0b0b0b;
    --paper: #ffffff;
    --accent: #f07328;
    --muted: #1a1a1a;
  }
  * { margin: 0; padding: 0; box-sizing: border-box; }
  html, body { width: 1200px; height: 892px; overflow: hidden; }
  body {
    background: var(--backdrop);
    font-family: "Quicksand", sans-serif;
    position: relative;
  }
  .card {
    position: absolute;
    top: 292px;
    width: 540px;
    height: 308px;
    overflow: hidden;
    box-shadow: 0 10px 28px rgba(0,0,0,.18);
  }

  /* ---------- contact side ---------- */
  .card--contact { left: 40px; background: var(--paper); color: var(--muted); }
  .card--contact .brand {
    position: absolute; left: 34px; top: 98px; width: 216px;
    display: flex; align-items: center; gap: 8px;
  }
  .brand__square { width: 14px; height: 14px; background: var(--accent); flex: none; }
  .card--contact .brand__name {
    font-family: "Montserrat", sans-serif; font-weight: 800;
    font-size: 32px; letter-spacing: 1.5px; color: var(--ink); white-space: nowrap;
  }
  .divider-top {
    position: absolute; left: 262px; top: 0; width: 30px; height: 138px;
    background: var(--accent);
  }
  .divider-top svg { position: absolute; left: 7px; bottom: 8px; }
  .divider-bottom {
    position: absolute; left: 262px; top: 272px; width: 30px; height: 36px;
    background: var(--accent);
  }
  .person { position: absolute; left: 306px; top: 98px; }
  .person__name {
    font-family: "Montserrat", sans-serif; font-weight: 700;
    font-size: 24px; letter-spacing: 3px; color: var(--ink); line-height: 1;
    white-space: nowrap;
  }
  .person__name .surname { color: var(--accent); }
  .person__role {
    font-family: "Montserrat", sans-serif; font-weight: 500;
    font-size: 13px; letter-spacing: 2.5px; margin-top: 6px;
  }
  .contacts { position: absolute; left: 262px; top: 158px; list-style: none; }
  .contacts li {
    display: flex; align-items: center; gap: 14px;
    height: 30px; font-size: 14.5px; font-weight: 500; letter-spacing: .4px;
    white-space: nowrap;
  }
  .contacts .icon {
    width: 24px; height: 24px; background: var(--accent); border-radius: 4px;
    display: flex; align-items: center; justify-content: center; flex: none;
  }

  /* ---------- brand side ---------- */
  .card--brand { left: 620px; background: var(--ink); color: var(--paper); }
  .card--brand .brand {
    position: absolute; left: 0; right: 0; top: 92px;
    display: flex; align-items: center; justify-content: center; gap: 12px;
  }
  .card--brand .brand__square { width: 20px; height: 20px; }
  .card--brand .brand__name {
    font-family: "Montserrat", sans-serif; font-weight: 800;
    font-size: 62px; letter-spacing: 3px; color: var(--paper); white-space: nowrap;
  }
  .bar { position: absolute; height: 11px; background: var(--accent); }
  .bar--short { left: 0; top: 196px; width: 150px; }
  .bar--long { left: 276px; top: 248px; width: 264px; }
  .website {
    position: absolute; left: 110px; top: 222px;
    font-size: 15px; font-weight: 500; letter-spacing: 2px;
  }
</style>
</head>
<body>

  <section class="card card--contact" aria-label="Business card, contact side">
    <div class="brand">
      <span class="brand__square"></span>
      <span class="brand__name">KORVANE</span>
    </div>

    <div class="divider-top">
      <svg width="16" height="16" viewBox="0 0 16 16" aria-hidden="true">
        <circle cx="8" cy="5" r="3.2" fill="#fff"/>
        <path d="M2 15c0-3.5 2.7-5.5 6-5.5s6 2 6 5.5z" fill="#fff"/>
      </svg>
    </div>
    <div class="divider-bottom"></div>

    <div class="person">
      <p class="person__name">JOHN <span class="surname">SMITH</span></p>
      <p class="person__role">CEO DIRECTOR</p>
    </div>

    <ul class="contacts">
      <li>
        <span class="icon">
          <svg width="14" height="14" viewBox="0 0 24 24" aria-hidden="true"><path fill="#fff" d="M6.6 10.8a15.1 15.1 0 0 0 6.6 6.6l2.2-2.2c.3-.3.7-.4 1-.2 1.1.4 2.3.6 3.6.6.6 0 1 .4 1 1V20c0 .6-.4 1-1 1A17 17 0 0 1 3 4c0-.6.4-1 1-1h3.5c.6 0 1 .4 1 1 0 1.3.2 2.5.6 3.6.1.3 0 .7-.2 1z"/></svg>
        </span>
        +000 123-456-789
      </li>
      <li>
        <span class="icon">
          <svg width="14" height="14" viewBox="0 0 24 24" aria-hidden="true"><rect x="2" y="5" width="20" height="14" rx="1.5" fill="none" stroke="#fff" stroke-width="2"/><path d="M3 6l9 7 9-7" fill="none" stroke="#fff" stroke-width="2"/></svg>
        </span>
        urname@email.com
      </li>
      <li>
        <span class="icon">
          <svg width="14" height="14" viewBox="0 0 24 24" aria-hidden="true"><path fill="#fff" d="M12 3l10 9h-3v9h-5v-6h-4v6H5v-9H2z"/></svg>
        </span>
        Your Street Address Here
      </li>
    </ul>
  </section>

  <section class="card card--brand" aria-label="Business card, brand side">
    <div class="brand">
      <span class="brand__square"></span>
      <span class="brand__name">KORVANE</span>
    </div>
    <div class="bar bar--short"></div>
    <p class="website">www.yoursite.com</p>
    <div class="bar bar--long"></div>
  </section>

</body>
</html>
```